broucher for electrical contracting buisness

use website template and attached files for colour scheme / ideas

Industry/Entity Type

Electrical

Requirements
Must have
• A5 folded to A4 4 pp format
• use the written content in the broucher word document as a guide

```html
<!DOCTYPE html>
<html lang="en">
<head>
<meta charset="utf-8">
<title>Corvell Electrical Brochure Spread</title>
<link rel="stylesheet" href="https://fonts.googleapis.com/css2?family=PT+Sans:wght@400;700&family=Saira+Semi+Condensed:wght@600;700&display=swap">
<style>
:root{
  --red:#e31e26;
  --navy:#1f2a5c;
  --ink:#222222;
  --rule-dark:#3a1e1e;
  --bg:#c8c8c8;
  --paper:#ffffff;
}
*{box-sizing:border-box;margin:0;padding:0}
html,body{width:1200px;height:977px;overflow:hidden;background:var(--bg)}
body{position:relative;font-family:"PT Sans",sans-serif;color:var(--ink)}
.spread{position:absolute;left:47px;top:100px;width:1107px;height:761px;background:var(--paper)}
.page{position:absolute;top:0;height:761px;width:553px}
.page--left{left:0}
.page--right{left:552px}
.abs{position:absolute}
.header-rule{position:absolute;top:40px;height:3px;background:var(--red)}
.brand{position:absolute;top:18px;width:190px;text-align:center;color:var(--navy);font-family:"Saira Semi Condensed",sans-serif;font-weight:700;line-height:1}
.brand__name{font-size:27px;letter-spacing:1px;display:block}
.brand__sub{font-size:9px;letter-spacing:3px;display:block;margin-top:2px}
.section-title{position:absolute;font-family:"Saira Semi Condensed",sans-serif;font-weight:700;color:var(--red);font-size:36px;line-height:1;letter-spacing:0}
.title-rule{position:absolute;height:3px}
.body-text{position:absolute;font-size:12.3px;line-height:19.3px}
.body-text p+p{margin-top:13px}
.photo{position:absolute}
.photo::after{content:"";position:absolute;inset:6px;border:1px solid rgba(255,255,255,.8)}
.checks{position:absolute;list-style:none;font-family:"Saira Semi Condensed",sans-serif;font-weight:600;color:var(--navy);font-size:15.5px}
.checks li{display:flex;align-items:center;height:27px;gap:4px}
.cta{position:absolute;left:72px;top:573px;width:406px;height:100px;border:1px solid #555}
.cta__inner{position:absolute;left:8px;top:8px;right:8px;bottom:8px;background:var(--red);color:#fff;font-family:"Saira Semi Condensed",sans-serif;font-weight:700;font-size:25px;line-height:29px;text-align:center;display:flex;align-items:center;justify-content:center}
.footer-rule{position:absolute;top:725px;height:2px;background:var(--navy);left:16px;width:518px}
.page--right .footer-rule{left:16px;width:522px}
.page-num{position:absolute;top:712px;width:27px;height:27px;border-radius:50%;background:var(--navy);color:#fff;font-size:13px;display:flex;align-items:center;justify-content:center;font-family:"Saira Semi Condensed",sans-serif}
.footer-text{position:absolute;top:728px;font-size:10.5px;color:var(--ink)}
.price{color:var(--red);font-weight:700}
</style>
</head>
<body>
<div class="spread">

  <section class="page page--left">
    <div class="header-rule" style="left:16px;width:168px"></div>
    <div class="header-rule" style="left:367px;width:167px"></div>
    <div class="brand" style="left:180px"><span class="brand__name">CORVELL</span><span class="brand__sub">ELECTRICAL · EC 24810</span></div>

    <h1 class="section-title" style="left:16px;top:80px">TEST TAG</h1>
    <div class="title-rule" style="left:16px;top:113px;width:97px;background:var(--red)"></div>
    <div class="title-rule" style="left:113px;top:113px;width:56px;background:var(--rule-dark)"></div>

    <div class="body-text" style="left:16px;top:128px;width:212px;text-align:justify">
      <p>Electrical testing and tagging is the process of determining if an electrical item is faulty. Our qualified electrician will visually inspect the item then perform a series of tests including:</p>
    </div>

    <ul class="checks" style="left:16px;top:248px">
      <li><svg width="14" height="14" viewBox="0 0 14 14"><circle cx="7" cy="7" r="5.5" fill="none" stroke="#e31e26" stroke-width="1.4"/><path d="M4.3 7.2l2 2 4.8-5" fill="none" stroke="#e31e26" stroke-width="1.5"/></svg>Insulation Resistance</li>
      <li><svg width="14" height="14" viewBox="0 0 14 14"><circle cx="7" cy="7" r="5.5" fill="none" stroke="#e31e26" stroke-width="1.4"/><path d="M4.3 7.2l2 2 4.8-5" fill="none" stroke="#e31e26" stroke-width="1.5"/></svg>Earth Circuit Test</li>
      <li><svg width="14" height="14" viewBox="0 0 14 14"><circle cx="7" cy="7" r="5.5" fill="none" stroke="#e31e26" stroke-width="1.4"/><path d="M4.3 7.2l2 2 4.8-5" fill="none" stroke="#e31e26" stroke-width="1.5"/></svg>Earth Leakage Tests</li>
      <li><svg width="14" height="14" viewBox="0 0 14 14"><circle cx="7" cy="7" r="5.5" fill="none" stroke="#e31e26" stroke-width="1.4"/><path d="M4.3 7.2l2 2 4.8-5" fill="none" stroke="#e31e26" stroke-width="1.5"/></svg>Polarity</li>
      <li><svg width="14" height="14" viewBox="0 0 14 14"><circle cx="7" cy="7" r="5.5" fill="none" stroke="#e31e26" stroke-width="1.4"/><path d="M4.3 7.2l2 2 4.8-5" fill="none" stroke="#e31e26" stroke-width="1.5"/></svg>RCD (Safety Switch) Test</li>
    </ul>

    <div class="photo" role="img" aria-label="Hands attaching a yellow test tag to an appliance plug beside a testing device" style="left:239px;top:129px;width:295px;height:232px;background:linear-gradient(135deg,#3b4a5a 0%,#8a96a3 45%,#d9cbb8 70%,#5d6670 100%)"></div>

    <div class="body-text" style="left:16px;top:395px;width:518px">
      <p>This process is then followed by placing an appliance tag on the electrical item which highlights to the operator that this has been serviced and is safe to use.</p>
      <p>All employers have a duty of care to provide a safe working environment from all hazards for all employees, visitor and Personal Under the Occupational Health and Safety Act Of 1984.</p>
      <p>Having your electrical equipment checked regularly will insure you are providing a safe working environment and avoiding possible electric shocks, fires. You also will avoid the legal ramification that follows.</p>
    </div>

    <div class="cta"><div class="cta__inner">OUR TEST TAG PRICES<br>START FROM $5.50 PER ITEM</div></div>

    <div class="footer-rule"></div>
    <div class="page-num" style="left:263px">04</div>
    <div class="footer-text" style="left:16px">info@corvellelectrical.com</div>
    <div class="footer-text" style="right:19px">www.corvellelectrical.com</div>
  </section>

  <section class="page page--right">
    <div class="header-rule" style="left:16px;width:169px"></div>
    <div class="header-rule" style="left:369px;width:169px"></div>
    <div class="brand" style="left:182px"><span class="brand__name">CORVELL</span><span class="brand__sub">ELECTRICAL · EC 24810</span></div>

    <h1 class="section-title" style="left:16px;top:80px">INDUSTRIAL</h1>
    <div class="title-rule" style="left:16px;top:113px;width:97px;background:var(--red)"></div>
    <div class="title-rule" style="left:113px;top:113px;width:97px;background:var(--rule-dark)"></div>

    <div class="photo" role="img" aria-label="Panoramic view of a red-earth mine site with cranes, conveyors and machinery" style="left:16px;top:132px;width:522px;height:202px;background:linear-gradient(180deg,#6a9ad0 0%,#a9c4e0 18%,#b25a32 30%,#c4744a 60%,#8a4a30 85%,#4d7a4a 100%)"></div>

    <div class="body-text" style="left:16px;top:358px;width:522px;text-align:justify">
      <p>We are committed to living our values of safety, quality, reliability, trust and loyalty. Our operations are characterised by strong safety, technical and project delivery performance whether in capital and major cities, regional towns or remote and challenging locations. With experience in major industrial projects across western Australia corvell electrical has the solution to your needs. We can tailor any installation to your specific requirements or industry specific needs.</p>
      <p>Please contact us regarding your next installation or maintenance needs.</p>
    </div>

    <h1 class="section-title" style="left:16px;top:515px">AIR CONDITIONING:</h1>
    <div class="title-rule" style="left:16px;top:549px;width:153px;background:var(--red)"></div>
    <div class="title-rule" style="left:169px;top:549px;width:153px;background:var(--rule-dark)"></div>

    <div class="body-text" style="left:16px;top:563px;width:522px">
      <p>Corvell Electrical takes pride in installing &amp; commissioning quality air conditioning systems, from installing a unit you have purchased to complete supply &amp; install packages.</p>
      <p>From <span class="price">$540*</span>, Corvell Electrical can arrange for a standard single storey back to back split system installation to suit most homes. Whether it’s a 2.5kW unit for smaller spaces or a 10kW for larger spaces, we can cater to your installation needs.</p>
    </div>

    <div class="footer-rule"></div>
    <div class="page-num" style="left:263px">05</div>
    <div class="footer-text" style="left:16px">info@corvellelectrical.com</div>
    <div class="footer-text" style="right:15px">www.corvellelectrical.com</div>
  </section>

</div>
</body>
</html>
```